Customer Upgrade from Free to Paid Investment Management

Our intent is to have customers that use our free online service consider converting into our paid investment management service.

In current vernacular, we have a Freemium business proposition - but we are just at the early stages of building out our upgrade capabilities.

The design request is detailed in the attached file, but essentially, I'm looking to add another banner to our library. Let me see what you can do!

Target Market(s)

40s-50s, can have any balance in their 401k, at first thought they could manage their 401k themselves, but may be interested in having us manage.

Industry/Entity Type

Investment

Requirements
Must have
• Keep it very simple.
Banner specs are attached in the file
Should not have
• No animation
No "hard sell"

```html
<!DOCTYPE html>
<html lang="en">
<head>
<meta charset="utf-8">
<title>Managed Investing Upgrade Banners</title>
<link rel="stylesheet" href="https://fonts.googleapis.com/css2?family=Arimo:wght@400;700&display=swap">
<style>
  :root {
    --page-bg: #ffffff;
    --banner-top: #f8a51d;
    --banner-bottom: #e36d0c;
    --text-light: #ffffff;
    --button-top: #7fd63a;
    --button-mid: #3fae12;
    --button-bottom: #2c8f08;
    --button-edge: #237a05;
    --arrow-disc: #f4f4f4;
    --arrow-mark: #1a1a1a;
    --art-screen-top: #d9e4ee;
    --art-screen-bottom: #7f9bb4;
    --art-advisor-top: #c9d2de;
    --art-advisor-bottom: #4f6a9a;
  }
  * { margin: 0; padding: 0; box-sizing: border-box; }
  html, body {
    width: 1200px;
    height: 545px;
    overflow: hidden;
    background: var(--page-bg);
    font-family: "Arimo", Arial, sans-serif;
  }
  .canvas { position: relative; width: 1200px; height: 545px; }

  .banner {
    position: absolute;
    left: 124px;
    width: 972px;
    height: 111px;
    background: linear-gradient(to bottom, var(--banner-top), var(--banner-bottom));
  }
  .banner--manage { top: 148px; }
  .banner--guidance { top: 323px; }

  .banner__art {
    position: absolute;
    border-radius: 8px;
  }
  .banner--manage .banner__art {
    left: 12px;
    top: -24px;
    width: 132px;
    height: 133px;
    background: linear-gradient(160deg, var(--art-screen-top), var(--art-screen-bottom));
  }
  .banner--guidance .banner__art {
    left: 24px;
    top: -22px;
    width: 130px;
    height: 132px;
    background: linear-gradient(160deg, var(--art-advisor-top), var(--art-advisor-bottom));
  }

  .banner__message {
    position: absolute;
    left: 179px;
    width: 500px;
    top: 0;
    height: 100%;
    display: flex;
    flex-direction: column;
    justify-content: center;
    align-items: center;
    color: var(--text-light);
    text-align: center;
    white-space: nowrap;
    gap: 5px;
  }
  .banner__headline { font-weight: 700; font-size: 28px; line-height: 1.1; }
  .banner__subline { font-weight: 400; font-size: 27px; line-height: 1.1; }

  .learn-more {
    position: absolute;
    left: 726px;
    top: 29px;
    width: 193px;
    height: 59px;
    border-radius: 30px;
    border: 2px solid var(--button-edge);
    background: linear-gradient(to bottom, var(--button-top) 0%, var(--button-mid) 50%, var(--button-bottom) 100%);
    box-shadow: inset 0 2px 2px rgba(255,255,255,0.45), 0 2px 3px rgba(0,0,0,0.25);
    display: flex;
    align-items: center;
    color: var(--text-light);
    text-decoration: none;
  }
  .learn-more__label {
    margin-left: 14px;
    font-weight: 700;
    font-size: 20px;
    letter-spacing: -0.3px;
    text-shadow: 0 1px 1px rgba(0,0,0,0.35);
  }
  .learn-more__arrow {
    position: absolute;
    right: 7px;
    top: 50%;
    transform: translateY(-50%);
    width: 42px;
    height: 42px;
  }
</style>
</head>
<body>
<main class="canvas">
  <section class="banner banner--manage">
    <div class="banner__art" role="img" aria-label="Illustration of a computer monitor with a settings gear"></div>
    <div class="banner__message">
      <p class="banner__headline">Want us to manage this for you?</p>
      <p class="banner__subline">You are in charge, we can do the work</p>
    </div>
    <a class="learn-more" href="#">
      <span class="learn-more__label">Learn More!</span>
      <svg class="learn-more__arrow" viewBox="0 0 42 42" aria-hidden="true">
        <circle cx="21" cy="21" r="20" fill="var(--arrow-disc)"/>
        <path d="M17 12 L26 21 L17 30" fill="none" stroke="var(--arrow-mark)" stroke-width="5" stroke-linecap="round" stroke-linejoin="round"/>
      </svg>
    </a>
  </section>

  <section class="banner banner--guidance">
    <div class="banner__art" role="img" aria-label="Illustration of a businessperson with a question mark"></div>
    <div class="banner__message">
      <p class="banner__headline">Not sure what to do from here?</p>
      <p class="banner__subline">It’s ok if you don’t know what to do next</p>
    </div>
    <a class="learn-more" href="#">
      <span class="learn-more__label">Learn More!</span>
      <svg class="learn-more__arrow" viewBox="0 0 42 42" aria-hidden="true">
        <circle cx="21" cy="21" r="20" fill="var(--arrow-disc)"/>
        <path d="M17 12 L26 21 L17 30" fill="none" stroke="var(--arrow-mark)" stroke-width="5" stroke-linecap="round" stroke-linejoin="round"/>
      </svg>
    </a>
  </section>
</main>
</body>
</html>
```